Vel Framewright - Worpress Design

We are a consultancy to help builders to optimize their planning in order to save building costs. For that reason we need a website to offer our services, present our history, the mission and offer a plug-in for a first contact (including calendar), testimonials, a blog etc.
As an idea, I really like: https://www.kestrumadvisory.de/
Later on the website should be programmed in www.wolkanet.de in our Wordpress area. The text, of course, will be done by myself. The colors should be suitable to our recently designed logo.

```html
<!DOCTYPE html>
<html lang="en">
<head>
<meta charset="utf-8">
<title>Vel Framewright – Consulting Services</title>
<link href="https://fonts.googleapis.com/css2?family=Audiowide&family=Ubuntu:wght@400;500&display=swap" rel="stylesheet">
<style>
:root{
  --gold:#e4a83a;
  --gold-light:#f0c25a;
  --gold-dark:#c27612;
  --cream:#fbeed6;
  --ink:#222;
  --muted:#555;
  --dark:#1e1e22;
  --white:#fff;
  --grey-btn:linear-gradient(90deg,#9a9a9a,#3e3e42);
  --gold-btn:linear-gradient(90deg,#f0c25a,#d68a18);
  --head:"Audiowide",sans-serif;
  --body:"Ubuntu",sans-serif;
}
*{margin:0;padding:0;box-sizing:border-box}
html,body{width:1200px;height:3448px;overflow:hidden;background:var(--white)}
body{font-family:var(--body);color:var(--ink)}
.page{position:relative;width:1200px;height:3448px;overflow:hidden}
.abs{position:absolute}
.svg-layer{position:absolute;left:0;top:0}
.photo{position:absolute}
.nav a{position:absolute;top:30px;font-size:12px;color:#eee;text-decoration:none}
.nav a.active{color:var(--gold-light);border-bottom:1px solid var(--gold-light)}
.brand{font-family:var(--body);font-weight:500;font-size:20px;color:var(--gold-light);display:flex;align-items:center;gap:10px}
.brand i{display:block;width:28px;height:28px;border:2px solid var(--gold-light)}
.btn{position:absolute;border-radius:20px;font-size:11px;color:#fff;display:flex;align-items:center;justify-content:center;text-decoration:none}
.btn.grey{background:var(--grey-btn)}
.btn.gold{background:var(--gold-btn)}
.btn.outline{border:1px solid #d8d8d8;color:#bbb;background:#fff}
.eyebrow{font-size:13px;text-align:center}
.h2{font-family:var(--head);font-size:17px;letter-spacing:2px;line-height:23px;text-transform:uppercase;text-align:center}
.on-gold .eyebrow,.on-gold .h2{color:#fff}
.gold-text{color:var(--gold-dark)}
.card{position:absolute;background:#fff;border-radius:4px;box-shadow:0 2px 8px rgba(0,0,0,.12);overflow:hidden}
.card .pic{height:135px}
.service h3{font-weight:400;font-size:13px;text-align:center;margin-top:16px;line-height:16px}
.service .btn{position:relative;margin:10px auto 0;width:96px;height:23px;font-size:10px}
.post .pic{height:154px}
.post .meta{font-size:10px;margin:22px 22px 0}
.post h3{font-size:13px;font-weight:500;margin:8px 22px 0;line-height:17px}
.post p{font-size:10px;margin:4px 22px 0;line-height:14px}
.post .btn{position:relative;margin:14px 22px 0;width:82px;height:24px;font-size:10px}
.arrow{position:absolute;font-size:16px;color:#fff}
.ring{position:absolute;border-radius:50%;border:3px solid var(--gold)}
.field{position:absolute;border:1px solid #e6e6e6;font-size:9px;color:#666;padding:9px 10px}
.footer h4{font-family:var(--head);font-size:12px;letter-spacing:1.5px;color:var(--gold);position:absolute}
.footer p,.footer li{font-size:11px;color:#fff;line-height:14px}
.footer ul{list-style:none}
.footer li{margin-bottom:6px}
</style>
</head>
<body>
<div class="page">

<!-- HERO -->
<div class="photo" role="img" aria-label="Team of consultants in a bright office meeting around laptops" style="left:0;top:0;width:1200px;height:600px;background:linear-gradient(135deg,#3a3a3e 0%,#6a6862 45%,#8d8a82 70%,#4c4a48 100%)"></div>
<svg class="svg-layer" width="1200" height="620" viewBox="0 0 1200 620" aria-hidden="true">
  <path d="M0 0H230C170 70 160 160 90 230C50 270 20 290 0 300Z" fill="#c9a867" opacity=".35"/>
  <path d="M740 0H1040C1020 90 960 140 880 150C790 160 730 90 740 0Z" fill="#c9a867" opacity=".35"/>
  <path d="M1100 0H1200V270C1140 250 1110 180 1120 110C1125 60 1105 30 1100 0Z" fill="#c9a867" opacity=".3"/>
  <path d="M0 330C40 470 130 580 300 592C560 608 780 420 1000 350C1090 320 1150 300 1200 285V620H0Z" fill="var(--cream)"/>
  <path d="M0 330C40 460 120 560 290 570C540 585 760 400 990 330C1080 302 1150 290 1200 280V600C1150 300 1080 320 990 350C760 420 560 590 300 585C130 575 40 470 0 380Z" fill="var(--gold)"/>
  <path d="M0 380C40 480 130 585 300 592C560 608 780 430 1000 360C1090 332 1150 320 1200 310V620H0Z" fill="var(--white)"/>
</svg>

<nav class="nav">
  <div class="brand abs" style="left:107px;top:24px"><i></i>Vel Framewright</div>
  <a class="active" style="left:503px">Home</a>
  <a style="left:558px">About Us</a>
  <a style="left:630px">Services</a>
  <a style="left:697px">Testimonials</a>
  <a style="left:788px">Blog</a>
  <a style="left:835px">Contact Us</a>
  <a class="btn grey" style="left:919px;top:19px;width:166px;height:36px;border-bottom:none">Get a Free Consultation</a>
</nav>

<div class="abs" style="left:200px;top:194px;font-family:var(--head);font-size:13px;letter-spacing:2px;color:var(--gold-light)">WELCOME TO VEL FRAMEWRIGHT</div>
<h1 class="abs" style="left:198px;top:222px;font-family:var(--head);font-weight:400;font-size:52px;line-height:62px;color:#fff;letter-spacing:2px">CONSULTING<br>SERVICES</h1>
<a class="btn gold" style="left:200px;top:363px;width:175px;height:37px;font-size:11px">Get a Free Consultation</a>
<svg class="abs" style="left:280px;top:516px" width="14" height="20" viewBox="0 0 14 20" aria-hidden="true"><path d="M7 1V18M2 13L7 18L12 13" stroke="#fff" stroke-width="1.6" fill="none"/></svg>

<!-- ABOUT -->
<div class="ring" style="left:229px;top:654px;width:324px;height:324px;border-width:2px"></div>
<div class="ring" style="left:240px;top:665px;width:302px;height:302px;border-width:8px;border-color:var(--gold)"></div>
<div class="photo" role="img" aria-label="Smiling consultant in a blue suit giving a thumbs up" style="left:248px;top:673px;width:286px;height:286px;border-radius:50%;background:linear-gradient(160deg,#cfd3d6,#5b6f8c 60%,#2c3e63)"></div>

<div class="abs" style="left:628px;top:696px;font-size:12px">About Us</div>
<div class="abs gold-text" style="left:628px;top:720px;font-family:var(--head);font-size:16px;letter-spacing:1.6px;line-height:23px">REASON FOR CHOOSING<br>OUR STRIKE CONSULTANCY</div>
<p class="abs" style="left:628px;top:779px;width:240px;font-size:10.5px;line-height:15px;color:var(--muted)">Lorem Ipsum is simply dummy text of the printing and typesetting industry.</p>
<p class="abs" style="left:628px;top:826px;width:345px;font-size:10.5px;line-height:15px;color:var(--muted)">Lorem Ipsum has been the industry's standard dummy text ever since the 1500s, when an unknown printer took a galley of type and scrambled it to make a type specimen book.</p>
<a class="btn grey" style="left:628px;top:900px;width:120px;height:38px">Explore More</a>

<!-- SERVICES -->
<svg class="svg-layer" style="top:900px" width="1200" height="720" viewBox="0 0 1200 720" aria-hidden="true">
  <defs><linearGradient id="goldband" x1="0" x2="1"><stop offset="0" stop-color="#efc154"/><stop offset="1" stop-color="#c27612"/></linearGradient></defs>
  <path d="M0 60C220 110 420 160 640 150C860 140 1040 60 1200 20V700C1060 680 880 670 640 680C400 690 200 700 0 700Z" fill="url(#goldband)"/>
  <path d="M0 716C220 660 420 600 700 590C920 582 1080 620 1200 640V720H0Z" fill="var(--cream)"/>
  <path d="M0 720C240 680 440 610 700 602C930 596 1080 630 1200 660V720Z" fill="#fff"/>
</svg>
<section class="on-gold">
  <div class="eyebrow abs" style="left:0;width:1200px;top:1114px">Our Services</div>
  <div class="h2 abs" style="left:0;width:1200px;top:1137px">Lorem Ipsum is dummy text of<br>the printing industry.</div>
</section>
<div class="card service" style="left:200px;top:1208px;width:182px;height:239px">
  <div class="pic" role="img" aria-label="Two colleagues reviewing a sales chart" style="background:linear-gradient(135deg,#e9ecef,#8a8f96)"></div>
  <h3>Sales<br>Management</h3><a class="btn outline">Read More</a>
</div>
<div class="card service" style="left:406px;top:1208px;width:182px;height:239px">
  <div class="pic" role="img" aria-label="Desktop monitor showing construction software" style="background:linear-gradient(135deg,#f2f2f2,#9a9a9a)"></div>
  <h3>Construction Software<br>&amp; Technology</h3><a class="btn outline">Read More</a>
</div>
<div class="card service" style="left:612px;top:1208px;width:182px;height:239px">
  <div class="pic" role="img" aria-label="Businessman with a house sketch behind him" style="background:linear-gradient(135deg,#f4f4f4,#6f7176)"></div>
  <h3>Home Builder<br>Marketing</h3><a class="btn gold">Read More</a>
</div>
<div class="card service" style="left:818px;top:1208px;width:182px;height:239px">
  <div class="pic" role="img" aria-label="Team shaking hands across a meeting table" style="background:linear-gradient(135deg,#e4e8ec,#596270)"></div>
  <h3>Employee<br>Engagement</h3><a class="btn outline">Read More</a>
</div>
<span class="arrow" style="left:482px;top:1485px">‹</span>
<a class="btn grey" style="left:536px;top:1477px;width:124px;height:38px">Discover More</a>
<span class="arrow" style="left:707px;top:1485px">›</span>

<!-- TESTIMONIALS -->
<div class="eyebrow abs" style="left:0;width:1200px;top:1659px">Testimonials</div>
<div class="h2 abs gold-text" style="left:0;width:1200px;top:1682px">Lorem Ipsum is dummy text of<br>the printing industry.</div>
<span class="abs" style="left:455px;top:1784px;font-size:18px;color:#333">‹</span>
<div class="photo" role="img" aria-label="Client portrait" style="left:498px;top:1772px;width:48px;height:48px;border-radius:50%;background:linear-gradient(135deg,#e0c7b3,#8a6a58)"></div>
<div class="ring" style="left:563px;top:1759px;width:74px;height:74px;border-width:2px"></div>
<div class="photo" role="img" aria-label="Client portrait" style="left:568px;top:1764px;width:64px;height:64px;border-radius:50%;background:linear-gradient(135deg,#f0dccb,#9c7560)"></div>
<div class="abs" style="left:589px;top:1820px;width:22px;height:22px;border-radius:50%;background:var(--gold);color:#fff;font-size:14px;text-align:center;line-height:24px">“</div>
<div class="photo" role="img" aria-label="Client portrait" style="left:655px;top:1772px;width:48px;height:48px;border-radius:50%;background:linear-gradient(135deg,#ddd,#6d6d6d)"></div>
<div class="abs" style="left:731px;top:1786px;width:18px;height:18px;border-radius:50%;background:var(--gold);color:#fff;font-size:13px;text-align:center;line-height:17px">›</div>
<p class="abs" style="left:290px;top:1860px;width:620px;text-align:center;font-size:13.5px;line-height:22.5px;color:#333">Lorem Ipsum is simply dummy text of the printing and typesetting industry. Lorem Ipsum has been the industry's standard dummy text ever since the 1500s, when an unknown printer took a galley of type and scrambled...</p>
<div class="abs" style="left:0;width:1200px;top:1938px;text-align:center;color:var(--gold);font-size:13px;letter-spacing:3px">★★★★★</div>
<div class="abs" style="left:0;width:1200px;top:1961px;text-align:center;font-size:10px;font-weight:500">Nora Jessup</div>

<!-- BLOG -->
<svg class="svg-layer" style="top:1930px" width="1200" height="760" viewBox="0 0 1200 760" aria-hidden="true">
  <defs><linearGradient id="goldband2" x1="0" x2="1"><stop offset="0" stop-color="#efc154"/><stop offset="1" stop-color="#c27612"/></linearGradient></defs>
  <path d="M0 40C220 90 440 120 700 110C920 100 1080 60 1200 30V700C1060 690 880 660 640 665C400 670 200 700 0 740Z" fill="url(#goldband2)"/>
  <path d="M0 0C300 40 520 110 760 105C960 100 1100 60 1200 40V70C1080 95 920 125 700 125C440 125 220 90 0 50Z" fill="var(--cream)"/>
  <path d="M0 0H1200V40C1100 60 960 100 760 105C520 110 300 40 0 0Z" fill="#fff"/>
</svg>
<section class="on-gold">
  <div class="eyebrow abs" style="left:0;width:1200px;top:2098px">Blog</div>
  <div class="h2 abs" style="left:0;width:1200px;top:2120px">Lorem Ipsum is dummy text of<br>the printing industry.</div>
</section>
<div class="card post" style="left:200px;top:2191px;width:250px;height:312px">
  <div class="pic" role="img" aria-label="Colleagues reviewing documents together" style="background:linear-gradient(135deg,#f1f1f1,#7b7f86)"></div>
  <div class="meta">July 11, 2023</div><h3>Delivering New Customer Experiences</h3><p>Lorem Ipsum is dummy text of the printing industry.</p><a class="btn outline">Read More</a>
</div>
<div class="card post" style="left:475px;top:2191px;width:250px;height:312px">
  <div class="pic" role="img" aria-label="Happy team giving thumbs up" style="background:linear-gradient(135deg,#f6f6f6,#6c6c70)"></div>
  <div class="meta">July 11, 2023</div><h3>Delivering New Customer Experiences</h3><p>Lorem Ipsum is dummy text of the printing industry.</p><a class="btn outline">Read More</a>
</div>
<div class="card post" style="left:750px;top:2191px;width:250px;height:312px">
  <div class="pic" role="img" aria-label="Colleagues celebrating with a high five" style="background:linear-gradient(135deg,#eef0ee,#5e6560)"></div>
  <div class="meta">July 11, 2023</div><h3>Delivering New Customer Experiences</h3><p>Lorem Ipsum is dummy text of the printing industry.</p><a class="btn gold">Read More</a>
</div>
<span class="arrow" style="left:482px;top:2543px">‹</span>
<a class="btn grey" style="left:536px;top:2535px;width:124px;height:38px">Discover More</a>
<span class="arrow" style="left:707px;top:2543px">›</span>

<!-- CONTACT -->
<div class="abs" style="left:215px;width:400px;top:2753px;text-align:center;font-size:12px">Get in touch</div>
<div class="abs gold-text" style="left:215px;width:400px;top:2776px;text-align:center;font-family:var(--head);font-size:17px;letter-spacing:2px">READY TO GET STARTED?</div>
<div class="field" style="left:212px;top:2819px;width:196px;height:32px">⚇&nbsp; Name</div>
<div class="field" style="left:212px;top:2863px;width:196px;height:32px">✉&nbsp; Email</div>
<div class="field" style="left:212px;top:2909px;width:196px;height:32px">▯&nbsp; Phone</div>
<div class="field" style="left:422px;top:2819px;width:197px;height:122px">▭&nbsp; Message</div>
<a class="btn grey" style="left:371px;top:2966px;width:87px;height:38px">Submit</a>
<div class="ring" style="left:666px;top:2717px;width:324px;height:324px;border-width:2px"></div>
<div class="ring" style="left:677px;top:2728px;width:302px;height:302px;border-width:8px"></div>
<div class="photo" role="img" aria-label="Smiling consultant in a blue suit giving a thumbs up" style="left:685px;top:2736px;width:286px;height:286px;border-radius:50%;background:linear-gradient(160deg,#cfd3d6,#5b6f8c 60%,#2c3e63)"></div>

<!-- FOOTER -->
<svg class="svg-layer" style="top:3050px" width="1200" height="398" viewBox="0 0 1200 398" aria-hidden="true">
  <path d="M0 110C120 40 320 10 560 30C820 50 1020 60 1200 40V398H0Z" fill="var(--gold)"/>
  <path d="M0 150C140 80 330 50 580 60C830 70 1020 80 1200 60V398H0Z" fill="#f4d48a"/>
  <path d="M0 180C150 110 340 80 600 85C840 90 1020 100 1200 85V398H0Z" fill="var(--dark)"/>
</svg>
<div class="photo" role="img" aria-label="Faint office team photo behind the footer" style="left:0;top:3140px;width:1200px;height:284px;background:linear-gradient(180deg,rgba(30,30,34,0),rgba(60,58,56,.5))"></div>
<footer class="footer">
  <div class="brand abs" style="left:200px;top:3265px"><i></i>Vel Framewright</div>
  <h4 style="left:402px;top:3216px">CONATCT INFO</h4>
  <div class="abs" style="left:402px;top:3243px;width:170px">
    <p style="padding-left:22px;position:relative"><span style="position:absolute;left:0;color:var(--gold)">⚲</span>412 Lorem ipsum Alder ln., Marlow, CA95100</p>
    <p style="padding-left:22px;margin-top:12px;position:relative"><span style="position:absolute;left:0;color:var(--gold)">✆</span>(555) 204-7731</p>
    <p style="padding-left:22px;margin-top:12px;position:relative"><span style="position:absolute;left:0;color:var(--gold)">✉</span>info@velframewright.de</p>
    <p style="padding-left:22px;margin-top:12px;position:relative"><span style="position:absolute;left:0;color:var(--gold)">◎</span>live location</p>
  </div>
  <h4 style="left:612px;top:3216px">QUICK LINK</h4>
  <ul class="abs" style="left:612px;top:3244px">
    <li style="color:var(--gold);text-decoration:underline">Home</li><li>About Us</li><li>Services</li><li>Testimonials</li><li>Blog</li><li>Contact Us</li>
  </ul>
  <h4 style="left:766px;top:3216px">STAY IN TOUCH</h4>
  <p class="abs" style="left:766px;top:3243px;width:200px;font-size:10px">Keep up with the latest news from the Vel Framewright</p>
  <div class="abs" style="left:763px;top:3284px;width:228px;height:27px;border:1px solid var(--gold);border-radius:14px;font-size:10px;color:#eee;padding:7px 14px">Your email address*</div>
  <a class="btn grey" style="left:763px;top:3325px;width:134px;height:29px">Subscribe Now</a>
</footer>
<div class="abs" style="left:0;top:3424px;width:1200px;height:24px;background:var(--gold)"></div>
<div class="abs" style="left:200px;top:3429px;font-size:9.5px;color:#222">© 2023 Vel Framewright. All Right Reserved</div>
<div class="abs" style="left:902px;top:3425px;width:18px;height:18px;border-radius:50%;background:#555"></div>
<div class="abs" style="left:928px;top:3425px;width:18px;height:18px;border-radius:50%;background:#555"></div>
<div class="abs" style="left:954px;top:3425px;width:18px;height:18px;border-radius:50%;background:#555"></div>
<div class="abs" style="left:981px;top:3425px;width:18px;height:18px;border-radius:50%;background:#555"></div>

</div>
</body>
</html>
```